Email Marketing Campaign 50% discount and buy-2-get-1 offer

I would like to inform my customers of our special offers via a e-Newsletter/Marketing E-Mail.

The coding needs to be done by the designer.

I have most of the design and the message that we wish to convey our buyers.

The information is:

1. We have now 50% discount on all our carpets

2. We have a buy-2 get-1 free carpet offer

For both the above messages we have already banner style that we like to use in our Newsletter.
I have attached the banner and the designers can use it.

3. We have opened a new shop in Berlin Germany

Therefore we like to have a Sylish Newsletter design that fits our website and products using the banner idea and we wish to include the 3 messages.
Special note should be given that this newsletter is going to our previous buyers. Therefore they already know us, and we just like to inform them of our latest news and offer.

Target Market(s)

Upmarket buyers looking for a great deal

Industry/Entity Type

Marketing

Coding

Coded - Design and coding required

Number of Pages Required

1 page

Font styles to use
Sans Serif

Colors
e667a6
34a7d8

Requirements
Must have
• Clear explanation with excitement in the message
Nice to have
• To promote clearly the 3 for 2 with maybe an explanation and clear images describing what the promotion is and how it works.
• I.e. buy 2 get 1 extra carpet of your choice free
• Add carpets to checkout and the system will calculate automatically
• The lowest carpet in your selection of 3 is the free carpet

```html
<!DOCTYPE html>
<html lang="en">
<head>
<meta charset="utf-8">
<title>Heirloom Rugs – We are in Berlin Now!</title>
<link rel="stylesheet" href="https://fonts.googleapis.com/css2?family=Open+Sans:wght@300;400;700;800&family=Arimo:wght@400&family=Bodoni+Moda:wght@400&family=Oswald:wght@300;400&family=Kaushan+Script&display=swap">
<style>
  :root {
    --pink: #e6007e;
    --yellow: #f7e81a;
    --ink: #3a3a3a;
    --grey: #7a7a7a;
    --light-grey: #c8c8c8;
    --footer: #454545;
    --footer-text: #ffffff;
    --footer-muted: #a8a8a8;
    --white: #ffffff;
  }
  * { margin: 0; padding: 0; box-sizing: border-box; }
  html, body { width: 1200px; height: 2645px; overflow: hidden; background: var(--white); }
  body { position: relative; font-family: "Open Sans", Arial, sans-serif; color: var(--ink); }

  .brand { position: absolute; top: 140px; left: 0; width: 1200px; display: flex; justify-content: center; align-items: center; gap: 18px; }
  .brand-dot { width: 22px; height: 22px; border-radius: 50%; background: var(--grey); }
  .brand-name { font-family: "Open Sans", sans-serif; font-weight: 400; font-size: 64px; color: var(--grey); letter-spacing: 2px; }

  .hero { position: absolute; top: 328px; left: 0; width: 1200px; height: 820px; overflow: hidden; }
  .hero-photo { position: absolute; inset: 0; background: linear-gradient(180deg, #cfc8bd 0%, #a89f93 45%, #5d4f4c 70%, #3f3436 100%); }
  .city-card { position: absolute; left: 625px; top: 30px; width: 520px; height: 330px; transform: rotate(-4deg); border: 12px solid var(--white); box-shadow: 0 6px 18px rgba(0,0,0,.35);
    background: linear-gradient(180deg, #2d6fa0 0%, #4a7ea8 40%, #6a4b3a 70%, #2b2230 100%); }
  .hero-arrow { position: absolute; left: 0; top: 0; width: 1200px; height: 820px; }
  .hero-lead { position: absolute; left: 175px; top: 440px; font-family: "Kaushan Script", cursive; font-size: 78px; color: var(--white); text-shadow: 0 2px 6px rgba(0,0,0,.35); white-space: nowrap; }
  .hero-title { position: absolute; left: 62px; top: 505px; font-family: "Kaushan Script", cursive; font-size: 170px; line-height: 1; color: var(--yellow); text-shadow: 0 3px 8px rgba(0,0,0,.35); white-space: nowrap; }

  .offer { position: absolute; top: 1223px; width: 471px; height: 471px; background: linear-gradient(160deg, #4a4440 0%, #2c2826 60%, #1f1c1b 100%); }
  .offer--half { left: 106px; border-top: 13px solid var(--pink); }
  .offer--three { left: 634px; border-top: 13px solid var(--yellow); }
  .offer-figure { position: absolute; left: 0; top: 30px; width: 100%; text-align: center; color: var(--white); white-space: nowrap; }
  .offer--half .offer-figure { font-family: "Bodoni Moda", serif; font-size: 240px; line-height: 1; }
  .offer--half .offer-figure small { font-size: 60px; vertical-align: 20px; margin-left: -10px; }

  .promo-kicker { position: absolute; top: 30px; left: 0; width: 100%; text-align: center; font-family: "Bodoni Moda", serif; font-size: 26px; letter-spacing: 2px; color: var(--white); }
  .promo-figure { position: absolute; top: 72px; left: 0; width: 100%; display: flex; justify-content: center; align-items: flex-start; gap: 10px; white-space: nowrap; color: var(--white); }
  .promo-digit { font-family: "Oswald", sans-serif; font-weight: 300; font-size: 190px; line-height: 1; }
  .promo-middle { display: flex; flex-direction: column; align-items: center; margin-top: 22px; }
  .promo-for { font-family: "Oswald", sans-serif; font-weight: 400; font-size: 96px; line-height: 1; letter-spacing: 2px; }
  .promo-script { font-family: "Kaushan Script", cursive; font-size: 48px; line-height: 1; margin-top: 2px; }

  .offer-box { position: absolute; left: 23px; top: 290px; width: 425px; height: 122px; display: flex; align-items: center; justify-content: center; text-align: center;
    font-family: "Arimo", Arial, sans-serif; font-size: 34px; line-height: 1.25; color: var(--white); }
  .offer--half .offer-box { border: 4px solid var(--pink); }
  .offer--three .offer-box { border: 4px solid var(--yellow); }

  .offer-caption { position: absolute; top: 1720px; width: 471px; text-align: center; font-size: 38px; line-height: 1.35; font-weight: 400; color: var(--ink); }
  .offer-caption strong { font-weight: 700; }
  .offer-caption--half { left: 106px; }
  .offer-caption--three { left: 634px; }

  .testimonial { position: absolute; top: 1906px; left: 80px; width: 1044px; height: 292px; }
  .bracket { position: absolute; top: 0; width: 44px; height: 292px; border: 3px solid var(--light-grey); }
  .bracket--left { left: 0; border-right: none; }
  .bracket--right { right: 0; border-left: none; }
  .quote-mark { position: absolute; font-family: "Open Sans", sans-serif; font-weight: 800; font-style: italic; font-size: 90px; line-height: 1; color: var(--grey); }
  .quote-mark--open { left: -16px; top: 12px; }
  .quote-mark--close { right: -16px; top: 128px; }
  .testimonial-label { position: absolute; top: 8px; left: 50%; transform: translateX(-50%); background: var(--light-grey); padding: 2px 16px 2px 28px; font-size: 17px; font-weight: 700; letter-spacing: 18px; color: var(--ink); white-space: nowrap; }
  .testimonial-title { position: absolute; top: 54px; left: 0; width: 100%; text-align: center; font-size: 29px; font-weight: 700; color: var(--ink); }
  .testimonial-body { position: absolute; top: 110px; left: 60px; width: 924px; text-align: center; font-size: 21px; line-height: 1.6; color: var(--ink); }
  .testimonial-author { position: absolute; top: 232px; left: 0; width: 100%; text-align: center; font-size: 20px; font-weight: 700; color: var(--ink); }

  .footer { position: absolute; top: 2259px; left: 0; width: 1200px; height: 386px; background: var(--footer); text-align: center; color: var(--footer-text); }
  .contact { position: absolute; left: 0; width: 100%; font-size: 28px; }
  .contact span { font-size: 20px; font-weight: 300; color: var(--footer-muted); margin-right: 8px; }
  .contact strong { font-weight: 700; }
  .contact--phone { top: 52px; }
  .contact--email { top: 96px; }
  .social { position: absolute; top: 168px; left: 0; width: 100%; display: flex; justify-content: center; gap: 26px; }
  .social-item { width: 50px; height: 50px; border-radius: 50%; background: #8a8a8a; }
  .website { position: absolute; top: 270px; left: 0; width: 100%; font-size: 34px; font-weight: 700; }
</style>
</head>
<body>
  <header class="brand">
    <span class="brand-dot"></span>
    <span class="brand-name">Heirloom Rugs</span>
  </header>

  <section class="hero">
    <div class="hero-photo" role="img" aria-label="Bright living room with a grey sofa and a faded vintage rug on a marble floor"></div>
    <div class="city-card" role="img" aria-label="Postcard photo of the Berlin skyline with the TV tower at dusk"></div>
    <svg class="hero-arrow" viewBox="0 0 1200 820" aria-hidden="true">
      <path d="M520 560 C600 470 680 410 760 365" fill="none" stroke="#e6007e" stroke-width="16" stroke-linecap="round"/>
      <polygon points="800,340 735,340 770,395" fill="#e6007e"/>
    </svg>
    <div class="hero-lead">We are in</div>
    <div class="hero-title">Berlin Now!</div>
  </section>

  <section class="offer offer--half" role="img" aria-label="Dark room photo behind the 50 percent offer">
    <div class="offer-figure">50<small>%</small></div>
    <div class="offer-box">Buy one carpet<br>get EXTRA 50% off</div>
  </section>
  <section class="offer offer--three" role="img" aria-label="Dark room photo behind the 3 for 2 coupon">
    <div class="promo-kicker">PROMOTION</div>
    <div class="promo-figure">
      <span class="promo-digit">3</span>
      <span class="promo-middle">
        <span class="promo-for">FOR</span>
        <span class="promo-script">Coupon</span>
      </span>
      <span class="promo-digit">2</span>
    </div>
    <div class="offer-box">Buy two carpets<br>get one free</div>
  </section>

  <p class="offer-caption offer-caption--half">Buy one carpet get<br><strong>EXTRA 50% off</strong></p>
  <p class="offer-caption offer-caption--three">Buy two carpets get<br><strong>One FREE</strong></p>

  <section class="testimonial">
    <div class="bracket bracket--left"></div>
    <div class="bracket bracket--right"></div>
    <div class="quote-mark quote-mark--open">“</div>
    <div class="quote-mark quote-mark--close">”</div>
    <div class="testimonial-label">TESTIMONIAL</div>
    <h2 class="testimonial-title">Great service, very quick delivery and beautiful carpets !</h2>
    <p class="testimonial-body">I have decided to order at heirloomrugs.com as they are specialist in this field and the rugs seemed great in quality. When it arrived, i was very pleased. Excellent size and the colours even more beautiful than i expected !</p>
    <p class="testimonial-author">– Marieke de Vos</p>
  </section>

  <footer class="footer">
    <p class="contact contact--phone"><span>Telephone :</span><strong>+ 44 203 555 0192</strong></p>
    <p class="contact contact--email"><span>Email :</span><strong>hello@heirloomrugs.com</strong></p>
    <div class="social" aria-label="Social channels">
      <span class="social-item"></span>
      <span class="social-item"></span>
      <span class="social-item"></span>
      <span class="social-item"></span>
      <span class="social-item"></span>
    </div>
    <p class="website">www.heirloomrugs.com</p>
  </footer>
</body>
</html>
```